UX Graphic design for a tablet - Commercial Vehicle Market

We need UX design for a 7"-10" tablet. We currently have a design for a mobile phone, but need a bigger design for tablet size.

We want to develop a landscape screen design for a 7”-10” tablet (needs to be compatible for both sizes). We have a current design that is (attached), but want to make some changes and come up with a better design. Maybe have the road temperature under the truck and the air temperature above the truck? We need it to be really easy to read as salt truck drivers look at these when they are plowing snow / putting salt on the roads.

Key requirements:
o Intuitive & easy to read display
o Air Temp
o Road Temp
o Truck on Road Graphic
o Truck Speed
o Plow Blade up/down
o Salt Spreader on/off
o Salt Spreading Rate
o Road Freeze Caution

```html
<!DOCTYPE html>
<html lang="en">
<head>
<meta charset="utf-8">
<title>Plow Pulse Monitor – Home</title>
<link href="https://fonts.googleapis.com/css2?family=Questrial&display=swap" rel="stylesheet">
<style>
  :root {
    --status-black: #0d0d0d;
    --accent-blue: #5ab6da;
    --nav-dark: #333333;
    --stop-red: #d8463f;
    --content-bg: #ededed;
    --card-white: #ffffff;
    --panel-dark: #3b3b3b;
    --panel-head: #4a4a4a;
    --text-dark: #333333;
    --text-light: #ffffff;
    --rule: #d9d9d9;
    --state-blue: #4aaed6;
    --state-red: #d0463f;
    --clock-blue: #6bb8dc;
    --ring-spread: #3cb4c6;
    --ring-air: #8bbd3f;
    --ring-road: #cf4843;
    --ring-speed: #c49a3f;
    --gauge-core: #2b2b2b;
    --truck-fill: #f4f4f4;
  }
  * { box-sizing: border-box; margin: 0; padding: 0; }
  html, body { width: 1200px; height: 752px; overflow: hidden; }
  body {
    position: relative;
    background: var(--content-bg);
    font-family: "Questrial", sans-serif;
    color: var(--text-dark);
  }

  /* status bar */
  .status-bar {
    position: absolute; left: 0; top: 0; width: 1200px; height: 20px;
    background: var(--status-black); color: var(--text-light);
    font-size: 13px; text-align: center; line-height: 20px;
    border-bottom: 4px solid var(--accent-blue); height: 24px;
  }
  .status-signal { position: absolute; left: 12px; top: 6px; }
  .status-battery { position: absolute; right: 14px; top: 7px; width: 14px; height: 8px; border: 1px solid var(--text-light); border-radius: 2px; }

  /* navigation */
  .main-nav { position: absolute; left: 0; top: 24px; width: 1200px; height: 83px; display: flex; }
  .nav-item {
    display: flex; align-items: center; justify-content: center; gap: 18px;
    color: var(--text-light); font-size: 30px; background: var(--nav-dark);
    text-decoration: none;
  }
  .nav-item svg { width: 44px; height: 44px; }
  .app-name { width: 215px; font-size: 19px; justify-content: center; }
  .nav-home { width: 242px; background: var(--accent-blue); }
  .nav-settings { width: 273px; }
  .nav-stop { width: 242px; background: var(--stop-red); }
  .nav-quit { width: 228px; }

  /* left column */
  .other-status {
    position: absolute; left: 27px; top: 152px; width: 265px; height: 203px;
    background: var(--card-white); border: 1px solid var(--rule);
  }
  .other-status-head { display: flex; align-items: center; height: 56px; border-bottom: 1px solid var(--rule); }
  .menu-tile { width: 56px; height: 56px; background: var(--nav-dark); display: flex; align-items: center; justify-content: center; }
  .other-status-title { font-size: 30px; margin-left: 10px; }
  .status-row { display: flex; height: 42px; align-items: center; border-bottom: 1px solid var(--rule); font-size: 19px; padding-left: 12px; }
  .status-row:last-child { border-bottom: none; }
  .status-label { width: 160px; }
  .state-on { color: var(--state-blue); }
  .state-caution { color: var(--state-red); }

  .clock-card {
    position: absolute; left: 27px; top: 374px; width: 265px; height: 256px;
    background: var(--clock-blue); color: var(--text-light); overflow: hidden;
  }
  .clock-text { position: absolute; right: 14px; top: 28px; text-align: right; font-size: 39px; line-height: 57px; }
  .clock-icon { position: absolute; left: -40px; top: 130px; width: 150px; height: 150px; }
  .version { position: absolute; left: 32px; top: 683px; font-size: 19px; color: var(--state-blue); }

  /* panels */
  .panel { position: absolute; left: 335px; width: 828px; background: var(--panel-dark); color: var(--text-light); }
  .panel-head { height: 25px; background: var(--panel-head); display: flex; align-items: center; font-size: 14px; }
  .panel-icon { width: 25px; height: 25px; display: flex; align-items: center; justify-content: center; margin: 0 22px 0 4px; }
  .truck-panel { top: 152px; height: 305px; }
  .temps-panel { top: 485px; height: 233px; }

  .truck-graphic {
    position: absolute; left: 60px; top: 61px; width: 445px; height: 208px;
    background: var(--truck-fill); border-radius: 14px 30px 8px 8px;
  }
  .callout { position: absolute; background: var(--accent-blue); color: var(--text-light); font-size: 30px; padding: 0 8px; line-height: 40px; }
  .callout-blade { left: 20px; top: 90px; }
  .callout-salt { left: 477px; top: 236px; }

  .gauge {
    position: absolute; border-radius: 50%; background: var(--gauge-core);
    display: flex; flex-direction: column; align-items: center; justify-content: center;
    color: var(--text-light);
  }
  .gauge-value { line-height: 1; }
  .gauge-unit { font-size: 18px; margin-top: 4px; }
  .gauge-spread { left: 576px; top: 53px; width: 220px; height: 220px; border: 16px solid var(--ring-spread); }
  .gauge-spread .gauge-value { font-size: 88px; }
  .gauge-temp { top: 47px; width: 164px; height: 164px; border: 14px solid; }
  .gauge-temp .gauge-value { font-size: 80px; }
  .gauge-air { left: 62px; border-color: var(--ring-air); }
  .gauge-road { left: 333px; border-color: var(--ring-road); }
  .gauge-speed { left: 625px; border-color: var(--ring-speed); }
  .gauge-note { position: absolute; top: 100px; font-size: 14px; line-height: 17px; }
  .note-air { left: 236px; }
  .note-road { left: 508px; }
</style>
</head>
<body>
  <header class="status-bar">
    <svg class="status-signal" width="16" height="8" viewBox="0 0 16 8"><path d="M0 8 L16 0 L16 8 Z" fill="#fff"/></svg>
    14:06 PM
    <span class="status-battery"></span>
  </header>

  <nav class="main-nav">
    <div class="nav-item app-name">Plow Pulse Monitor</div>
    <a class="nav-item nav-home" href="#">
      <svg viewBox="0 0 44 44" fill="none" stroke="#fff" stroke-width="2.5"><path d="M4 22 L22 5 L40 22"/><path d="M9 18 V40 H18 V28 H26 V40 H35 V18"/></svg>Home</a>
    <a class="nav-item nav-settings" href="#">
      <svg viewBox="0 0 44 44" fill="none" stroke="#fff" stroke-width="2.5"><circle cx="22" cy="22" r="7"/><path d="M19 4 H25 L26 9 L31 11 L35 8 L39 12 L36 17 L38 21 L40 22 V25 L35 26 L33 31 L36 35 L32 39 L27 36 L23 38 L22 40 H19 L18 35 L13 33 L9 36 L5 32 L8 27 L6 23 L4 22 V19 L9 18 L11 13 L8 9 L12 5 L17 8 Z"/></svg>Settings</a>
    <a class="nav-item nav-stop" href="#">
      <svg viewBox="0 0 44 44" fill="none" stroke="#fff" stroke-width="4" stroke-linecap="round"><path d="M14 11 A15 15 0 1 0 30 11"/><path d="M22 5 V22"/></svg>Stop</a>
    <a class="nav-item nav-quit" href="#">
      <svg viewBox="0 0 44 44" fill="none" stroke="#fff" stroke-width="2.5"><path d="M26 14 V5 H6 V39 H26 V30"/><path d="M16 22 H40 M33 15 L40 22 L33 29"/></svg>Quit</a>
  </nav>

  <section class="other-status">
    <div class="other-status-head">
      <div class="menu-tile">
        <svg width="28" height="22" viewBox="0 0 28 22" fill="#fff"><rect y="0" width="28" height="4"/><rect y="9" width="28" height="4"/><rect y="18" width="28" height="4"/></svg>
      </div>
      <span class="other-status-title">Other Status</span>
    </div>
    <div class="status-row"><span class="status-label">Salt Spreader</span><span class="state-on">ON</span></div>
    <div class="status-row"><span class="status-label">Road Freeze</span><span class="state-caution">Caution</span></div>
    <div class="status-row"><span class="status-label">Blade</span><span class="state-on">Down</span></div>
  </section>

  <section class="clock-card">
    <svg class="clock-icon" viewBox="0 0 150 150" fill="none" stroke="#fff" stroke-width="12"><circle cx="75" cy="75" r="62"/><path d="M75 38 V80 H105" stroke-width="10"/></svg>
    <div class="clock-text">02:45 AM<br>November<br>17th<br>2014</div>
  </section>

  <p class="version">Version: 2014-07-02 09.00</p>

  <section class="panel truck-panel">
    <div class="panel-head">
      <span class="panel-icon"><svg width="18" height="18" viewBox="0 0 18 18" fill="none" stroke="#bbb" stroke-width="1.5"><circle cx="9" cy="9" r="7.5"/><circle cx="9" cy="9" r="2.5"/></svg></span>
      Truck Status
    </div>
    <div class="truck-graphic" role="img" aria-label="White side-view illustration of a plow truck with front blade and rear salt spreader"></div>
    <span class="callout callout-blade">Blade</span>
    <span class="callout callout-salt">Salt</span>
    <div class="gauge gauge-spread"><span class="gauge-value">349</span><span class="gauge-unit">Spread Rate</span></div>
  </section>

  <section class="panel temps-panel">
    <div class="panel-head">
      <span class="panel-icon"><svg width="10" height="20" viewBox="0 0 10 20" fill="none" stroke="#bbb" stroke-width="1.5"><rect x="3" y="1" width="4" height="13" rx="2"/><circle cx="5" cy="16" r="3"/></svg></span>
      Temperatures
    </div>
    <div class="gauge gauge-temp gauge-air"><span class="gauge-value">72</span><span class="gauge-unit">Air-Temp</span></div>
    <p class="gauge-note note-air">Air<br>Temperature<br>status</p>
    <div class="gauge gauge-temp gauge-road"><span class="gauge-value">72</span><span class="gauge-unit">Road-Temp</span></div>
    <p class="gauge-note note-road">Road<br>Temperature<br>status</p>
    <div class="gauge gauge-temp gauge-speed"><span class="gauge-value">50</span><span class="gauge-unit">Mph</span></div>
  </section>
</body>
</html>
```